Bluewater Getaways KT needs a new Website

We have an old website that is just that - old. We need a fresh website that is professional graphic designed that has the following features.
1. Can be updated by ourselves in some areas.
2. Has a shopping cart.
3. Has links to download PDF files
4. Has links to other pages in the website
5. Includes social media links
6. Has a client log-in area
Full details in brief provided.

SORRY BUT IT'S URGENT. We've taken too long to write the details and it is now urgent. So my apologies I will be asking for designers to work quickly.

We will continue to use our existing web hosting company and url. Their is a link to the old website in the Design Brief.
Updates

UPDATE:  Please see the new file UPDATE TO DESIGN BRIEF.
Thanks for all your submissions to date.  We hope the update will assist with your designs.
As indicated in previous messages, we are happy with the Home Page + 1 Page in order to select the designer to work with in creating the full design. 

Thankyou Designers.  Much appreciate your efforts.
It's getting late here on Kestrel so I won't have much chance too review any more designs this evening.
But for your information:
Designer 7318405 Ravindra Mehta is so far the closest to what we are seeking.
Thanks again. 

Reason: Have extended to Monday 7 October to give time for designers to submit after feedback today. Especially given the time differences

Target Market(s)

Very wide audience. Current client group not that tech savvy, but we hope to broaden our market and sell more creative products, and so website needs to consider how people now use media, ie tablets & iphones.

Industry/Entity Type

Shopping

Requirements
Nice to have
• PLEASE SEE THE "UPDATE TO THE DESIGN BRIEF"

```html
<!DOCTYPE html>
<html lang="en">
<head>
<meta charset="utf-8">
<title>Bluewater Getaways KT — Home</title>
<link rel="stylesheet" href="https://fonts.googleapis.com/css2?family=Roboto:wght@300;400;700&display=swap">
<style>
:root{
  --sand:#f7e9dd;
  --white:#ffffff;
  --panel:#fafafa;
  --footer:#f0f0f0;
  --text:#2a2a2a;
  --muted:#555555;
  --green:#15a34a;
  --orange:#f08a24;
  --link:#2046b8;
  --line:#d8d8d8;
}
*{box-sizing:border-box;margin:0;padding:0}
html,body{width:1200px;height:1044px;overflow:hidden}
body{font-family:"Roboto",Arial,sans-serif;color:var(--text);
  background:linear-gradient(to bottom,var(--white) 0,var(--white) 200px,var(--sand) 290px,var(--sand) 100%);
  position:relative}
.abs{position:absolute}
.deco-flipflops{left:920px;top:0;width:280px;height:300px;
  background:radial-gradient(ellipse at 60% 40%,#8fd44a 0,#7cc63a 45%,rgba(247,233,221,0) 75%)}
.deco-shells-left{left:0;top:200px;width:250px;height:100px;
  background:radial-gradient(ellipse at 50% 60%,#b47a55 0,#d8b49a 40%,rgba(247,233,221,0) 75%)}
.deco-shells-right{left:950px;top:200px;width:250px;height:100px;
  background:radial-gradient(ellipse at 50% 60%,#b47a55 0,#d8b49a 40%,rgba(247,233,221,0) 75%)}

.brand{left:0;width:1200px;top:24px;display:flex;justify-content:center;align-items:center;gap:10px}
.brand-dot{width:34px;height:34px;border-radius:50%;background:var(--orange)}
.brand-name{font-weight:700;font-size:22px;color:var(--orange);letter-spacing:.5px}

.main-nav{top:95px;left:300px;display:flex;gap:0;font-size:12px}
.main-nav a{color:var(--text);text-decoration:none;padding:6px 16px;line-height:13px}
.main-nav a.active{background:var(--green);color:var(--white);padding:6px 9px}

.hero{left:248px;top:140px;width:704px;height:234px;
  background:linear-gradient(to bottom,#2f6fc2 0,#6aa9e0 35%,#3d8a68 45%,#34c6cf 55%,#7fe3db 100%);
  box-shadow:0 1px 3px rgba(0,0,0,.25)}
.hero-copy{position:absolute;right:66px;top:68px;text-align:right;color:var(--white)}
.hero-title{font-weight:700;font-size:28px;line-height:30px}
.hero-sub{font-weight:300;font-size:14px;line-height:16px;margin-bottom:6px}
.hero-arrow{position:absolute;top:98px}
.hero-dots{position:absolute;left:0;width:100%;top:205px;display:flex;justify-content:center;gap:8px}
.hero-dots span{width:14px;height:14px;border-radius:50%;background:var(--white);border:2px solid rgba(255,255,255,.6)}
.hero-dots span.on{background:var(--orange);border-color:var(--white)}

.section-title{left:0;width:1200px;top:382px;text-align:center;font-weight:300;font-size:22px;color:#444}
.carousel-btn{top:386px;width:26px;height:26px;border-radius:50%;background:var(--white);
  box-shadow:0 1px 2px rgba(0,0,0,.2);display:flex;align-items:center;justify-content:center}

.card{top:424px;width:228px;height:138px;background:var(--white);padding:2px;box-shadow:0 1px 3px rgba(0,0,0,.2)}
.card-photo{width:100%;height:100%;position:relative}
.card-label{position:absolute;left:0;bottom:0;width:100%;height:32px;background:rgba(255,255,255,.78);
  text-align:center;font-size:17px;line-height:32px;color:#222}

.info-panel{left:246px;top:584px;width:708px;height:182px;background:var(--white);
  background:linear-gradient(to bottom,#fff,#f7f7f7)}
.info-divider{left:709px;top:584px;width:1px;height:182px;background:var(--line)}
.portrait{left:268px;top:606px;width:98px;height:98px;background:var(--white);padding:2px;box-shadow:0 1px 3px rgba(0,0,0,.3)}
.portrait div{width:100%;height:100%;background:linear-gradient(to bottom,#4f86b8,#6e5a3e)}
.mission{left:382px;top:662px;width:320px;font-size:8.5px;line-height:10.5px}
.mission strong{display:block;margin-bottom:10px}

.newsletter-title{left:725px;top:606px;font-size:17px;font-weight:400}
.newsletter-form{left:726px;top:632px;display:flex}
.newsletter-form .field{width:176px;height:22px;border:1px solid #ccc;background:var(--white);font-size:9px;color:#999;padding:5px 6px}
.newsletter-form .send{width:34px;height:22px;background:var(--orange);color:var(--white);font-weight:700;font-size:9.5px;line-height:22px;text-align:center}
.phone-list{font-size:8.5px;color:#333}
.phone-list li{list-style:none;display:flex;align-items:center;gap:5px;height:18px}
.phone-icon{width:7px;height:9px}
.pay-cards{left:726px;top:728px;display:flex;gap:2px}
.pay-cards span{width:27px;height:16px;border-radius:2px;border:1px solid #ccc}

.site-footer{left:246px;top:766px;width:708px;height:212px;background:var(--footer);border-top:1px solid #e2e2e2;border-bottom:1px solid #d5d5d5}
.col-title{font-size:11.5px;font-weight:400;color:#222;letter-spacing:.2px}
.map{left:264px;top:806px;width:136px;height:107px;background:linear-gradient(135deg,#e4e2dc,#d6d9cf);border:2px solid var(--white);box-shadow:0 1px 2px rgba(0,0,0,.2)}
.address{left:264px;top:920px;font-size:8.5px;line-height:11px;color:#444}
.address strong{color:#222}
.dots-v{top:804px;height:132px;border-left:2px dotted #888}
.web-links{left:444px;top:905px;font-size:8.5px;line-height:13.5px;color:#555}
.web-links a{color:var(--link);text-decoration:none}
.thumbs{left:629px;top:804px;display:grid;grid-template-columns:repeat(3,34px);gap:8px 9px}
.thumbs span{height:34px;border:2px solid var(--white);box-shadow:0 1px 2px rgba(0,0,0,.25)}
.social-link{left:631px;top:932px;display:flex;align-items:center;gap:6px;color:#3b5a9a}
.social-link .sq{width:18px;height:18px;background:#3b5a9a}
.social-link .txt{font-size:14px;line-height:15px}
.social-link .txt small{display:block;font-size:10px}
.side-img{left:801px;width:128px;border:2px solid var(--white);box-shadow:0 1px 2px rgba(0,0,0,.3)}
.side-caption{left:801px;width:128px;text-align:center;font-size:11.5px;color:#222}

.bottom-nav{left:246px;top:991px;display:flex;gap:19px;font-size:8.5px}
.bottom-nav a{color:#333;text-decoration:none}
.legal{left:700px;width:257px;top:991px;text-align:right;font-size:8.5px;line-height:12.5px;color:#333}
</style>
</head>
<body>

<div class="abs deco-shells-left" role="img" aria-label="Seashells resting on sand"></div>
<div class="abs deco-shells-right" role="img" aria-label="Seashells resting on sand"></div>
<div class="abs deco-flipflops" role="img" aria-label="Green flip-flops with pink straps and white sunglasses"></div>

<header class="abs brand">
  <span class="brand-dot"></span>
  <span class="brand-name">Bluewater Getaways KT</span>
</header>

<nav class="abs main-nav">
  <a class="active" href="#">Home</a>
  <a href="#">Kestrel Tor</a>
  <a href="#">Services Holiday Programs</a>
  <a href="#">Our Shop</a>
  <a href="#">Make a Booking</a>
  <a href="#">Testimonials</a>
</nav>

<section class="abs hero" role="img" aria-label="Turquoise lagoon with pine-covered island under blue sky">
  <svg class="hero-arrow" style="left:16px" width="22" height="40" viewBox="0 0 22 40"><path d="M20 1 2 20l18 19" fill="none" stroke="#fff" stroke-width="1.5"/></svg>
  <svg class="hero-arrow" style="right:16px" width="22" height="40" viewBox="0 0 22 40"><path d="M2 1l18 19L2 39" fill="none" stroke="#fff" stroke-width="1.5"/></svg>
  <div class="hero-copy">
    <div class="hero-title">OUR SOCIAL ENTERPRISE</div>
    <div class="hero-sub">ESTABLISHED JULY 2001</div>
    <div class="hero-title">PROMOTES</div>
    <div class="hero-sub">ESTABLISHED JULY 2001</div>
  </div>
  <div class="hero-dots"><span class="on"></span><span></span><span></span></div>
</section>

<h2 class="abs section-title">Supported</h2>
<div class="abs carousel-btn" style="left:900px"><svg width="8" height="12" viewBox="0 0 8 12"><path d="M7 1 2 6l5 5" fill="none" stroke="#333" stroke-width="1.4"/></svg></div>
<div class="abs carousel-btn" style="left:929px"><svg width="8" height="12" viewBox="0 0 8 12"><path d="M1 1l5 5-5 5" fill="none" stroke="#333" stroke-width="1.4"/></svg></div>

<article class="abs card" style="left:246px">
  <div class="card-photo" role="img" aria-label="Kayaker paddling in clear rocky bay" style="background:linear-gradient(to bottom,#6f8fa8,#3aa0c8 50%,#6cc7d6)">
    <div class="card-label">HOLIDAYS</div>
  </div>
</article>
<article class="abs card" style="left:486px">
  <div class="card-photo" role="img" aria-label="Group riding camels along a beach" style="background:linear-gradient(to bottom,#3b7fd0,#8fb8e6 50%,#c9a57a)">
    <div class="card-label">TRAVEL</div>
  </div>
</article>
<article class="abs card" style="left:726px">
  <div class="card-photo" role="img" aria-label="Cheerful group waving under trees" style="background:linear-gradient(to bottom,#6e8a3a,#b08a6a 55%,#d9b9a9)">
    <div class="card-label">RECREATION</div>
  </div>
</article>

<section class="abs info-panel"></section>
<div class="abs info-divider"></div>
<div class="abs portrait"><div role="img" aria-label="Portrait of a man holding a large fish by the sea"></div></div>
<p class="abs mission"><strong>for people requiring support to participate in socially inclusive events.</strong>Intellectual Disability / Acquired Brain Injury / Mental Health / Sensory Impairment / Frail Aged / Mobility Challenged / Siblings of children with Disabilities</p>

<h3 class="abs newsletter-title">NEWSLETTER</h3>
<form class="abs newsletter-form"><div class="field">Enter your email address</div><div class="send">SEND</div></form>
<ul class="abs phone-list" style="left:728px;top:662px">
  <li><svg class="phone-icon" viewBox="0 0 7 9"><path d="M2 0h1.5v2.5H2.5Q2 4.5 3 6.5h1V9H2.5Q0 6 1 1z" fill="#222"/></svg>International + 61 55 01942</li>
  <li><svg class="phone-icon" viewBox="0 0 7 9"><path d="M2 0h1.5v2.5H2.5Q2 4.5 3 6.5h1V9H2.5Q0 6 1 1z" fill="#222"/></svg>Australia 1800 555 019</li>
  <li><svg class="phone-icon" viewBox="0 0 7 9"><path d="M2 0h1.5v2.5H2.5Q2 4.5 3 6.5h1V9H2.5Q0 6 1 1z" fill="#222"/></svg>New Zealand</li>
</ul>
<div class="abs pay-cards"><span style="background:#f4f4f4"></span><span style="background:#f2c877"></span><span style="background:#1d3f8f"></span><span style="background:#f4f4f4"></span><span style="background:#2f7fc6"></span></div>

<footer class="abs site-footer"></footer>
<h4 class="abs col-title" style="left:267px;top:783px">LOCATION &amp; CONTACTS</h4>
<div class="abs map" role="img" aria-label="Street map of the office location"></div>
<p class="abs address"><strong>Heron Lane,</strong> Pine Cove<br>PO Box 514 Kestrel Tor<br>KTR 2950 SOUTH PACIFIC<br>N.B.N. 410 227 586</p>

<div class="abs dots-v" style="left:422px"></div>
<h4 class="abs col-title" style="left:446px;top:783px">TELEPHONE</h4>
<ul class="abs phone-list" style="left:446px;top:808px">
  <li><svg class="phone-icon" viewBox="0 0 7 9"><path d="M2 0h1.5v2.5H2.5Q2 4.5 3 6.5h1V9H2.5Q0 6 1 1z" fill="#222"/></svg>International + 61 55 01942</li>
  <li><svg class="phone-icon" viewBox="0 0 7 9"><path d="M2 0h1.5v2.5H2.5Q2 4.5 3 6.5h1V9H2.5Q0 6 1 1z" fill="#222"/></svg>Australia 1800 555 019</li>
  <li><svg class="phone-icon" viewBox="0 0 7 9"><path d="M2 0h1.5v2.5H2.5Q2 4.5 3 6.5h1V9H2.5Q0 6 1 1z" fill="#222"/></svg>New Zealand</li>
</ul>
<h4 class="abs col-title" style="left:446px;top:875px">WEBSITE &amp; FRIENDBOOK</h4>
<p class="abs web-links">hello@bluewatergetaways.org<br>www.bluewatergetaways.org<br><a href="#">www.friendbook.com/bluewater<br>getaways</a></p>

<div class="abs dots-v" style="left:600px"></div>
<h4 class="abs col-title" style="left:629px;top:783px">IMAGE &amp; VIDEO</h4>
<div class="abs thumbs" role="img" aria-label="Gallery of holiday photo and video thumbnails">
  <span style="background:#6b7f8c"></span><span style="background:#5f95b8"></span><span style="background:#9bab6f"></span>
  <span style="background:#5a5450"></span><span style="background:#d8d8d8"></span><span style="background:#b57a68"></span>
  <span style="background:#5a6b55"></span><span style="background:#6a6a48"></span><span style="background:#4b7fb8"></span>
</div>
<a class="abs social-link" href="#"><span class="sq"></span><span class="txt"><small>Find us on</small>Friendbook</span></a>

<div class="abs dots-v" style="left:777px"></div>
<h4 class="abs col-title" style="left:813px;top:783px">OPEN REEL FILM FESTIVAL</h4>
<div class="abs side-img" style="top:806px;height:59px;background:radial-gradient(circle,#e8b23c 0,#d8441c 45%,#a8200e 100%)" role="img" aria-label="Golden film reel on red background"></div>
<div class="abs side-caption" style="top:876px">Support Us</div>
<div class="abs side-img" style="top:895px;height:59px;background:linear-gradient(135deg,#7a3a22,#d59a7c 55%,#8a4a30)" role="img" aria-label="Hands joined in support"></div>

<nav class="abs bottom-nav">
  <a href="#">Home</a><a href="#">Kestrel Tor</a><a href="#">Services Holiday Programs</a><a href="#">Our Shop</a><a href="#">Make a Booking</a><a href="#">Testimonials</a>
</nav>
<p class="abs legal">© 2013 Bluewater Getaways. All Rights Reserved<br>Designed by Brightline Studio</p>

</body>
</html>
```